Business card design and logo for hot water plumbing business

I need a logo and business card for my business which installs hot water heaters
Must have on front:
Paramount Hot Water Services
Gareth Pellow
0498163204

Either front or back:
gareth@paramounthotwaterservices-example.com.au
ABN 48207153690
Licence No 538412K

On the back in point form:
Supply and installation of
• electric storage
• gas storage/instantaneous
• heat pumps
• solar heaters

Iv provided 3 examples of cards I like but open to different ideas.

```html
<!DOCTYPE html>
<html lang="en">
<head>
<meta charset="utf-8">
<title>Paramount Hot Water Services – Business Card</title>
<link rel="stylesheet" href="https://fonts.googleapis.com/css2?family=Questrial&family=Mulish:wght@700;800&display=swap">
<style>
  :root {
    --page-bg: #ece8e3;
    --card-white: #ffffff;
    --blue-deep: #0b7bc4;
    --blue-light: #74c1ee;
    --panel-blue: #7cc4ef;
    --ink: #1d1d1f;
    --ink-soft: #2a2f36;
    --brand-ink: #3d4650;
  }
  * { box-sizing: border-box; margin: 0; padding: 0; }
  html, body {
    width: 1200px; height: 899px; overflow: hidden;
    background: var(--page-bg);
  }
  .stage { position: relative; width: 1200px; height: 899px; }

  .card {
    position: absolute;
    width: 560px; height: 320px;
    background: var(--card-white);
    transform: scale(1.196);
    transform-origin: 0 0;
    overflow: hidden;
    box-shadow: 0 2px 8px rgba(0,0,0,0.12);
  }
  .card--front { left: 153px; top: 60px; }
  .card--back  { left: 374px; top: 455px; }

  .card__bands { position: absolute; inset: 0; width: 560px; height: 320px; }

  .brand {
    position: absolute; display: flex; flex-direction: column; align-items: center;
    font-family: "Mulish", sans-serif; font-weight: 800; color: var(--brand-ink);
    white-space: nowrap;
  }
  .brand__mark { border-radius: 50%; background: var(--blue-deep); }
  .brand--front { left: 0; width: 560px; top: 80px; font-size: 17px; }
  .brand--front .brand__mark { width: 78px; height: 78px; margin-bottom: 24px; }
  .brand--back { left: 20px; width: 175px; top: 28px; font-size: 10.5px; }
  .brand--back .brand__mark { width: 36px; height: 36px; margin-bottom: 10px; }

  .holder {
    position: absolute; left: 48px; top: 240px;
    font-family: "Questrial", sans-serif; color: var(--ink);
    font-size: 21px; line-height: 25px;
  }

  .panel { position: absolute; background: var(--panel-blue); }
  .panel--contact {
    left: 200px; top: 0; width: 360px; height: 132px;
    border-bottom-left-radius: 42px;
    padding: 57px 0 0 22px;
    font-family: "Questrial", sans-serif; color: var(--ink-soft);
    font-size: 12px; line-height: 17px; white-space: nowrap;
  }
  .panel--services {
    left: 0; top: 147px; width: 315px; height: 173px;
    border-top-right-radius: 42px;
    padding: 30px 0 0 35px;
    font-family: "Mulish", sans-serif; font-weight: 700; color: var(--ink);
  }
  .services__title { font-size: 16.5px; line-height: 22px; }
  .services__list { list-style: none; font-size: 15px; line-height: 21px; }
  .services__list li::before { content: "• "; }
</style>
</head>
<body>
<main class="stage">

  <section class="card card--front" aria-label="Business card front">
    <svg class="card__bands" viewBox="0 0 560 320" aria-hidden="true">
      <polygon points="0,0 560,0 560,55 140,10 0,20" fill="var(--blue-deep)"/>
      <polygon points="0,20 140,10 560,55 560,66 140,23 0,40" fill="var(--blue-light)"/>
      <polygon points="0,272 380,292 560,255 560,268 380,305 0,287" fill="var(--blue-light)"/>
      <polygon points="0,287 380,305 560,268 560,320 0,320" fill="var(--blue-deep)"/>
    </svg>
    <div class="brand brand--front">
      <span class="brand__mark"></span>
      <span class="brand__name">Paramount Hot Water Services</span>
    </div>
    <div class="holder">
      <p class="holder__name">Gareth Pellow</p>
      <p class="holder__phone">0498163204</p>
    </div>
  </section>

  <section class="card card--back" aria-label="Business card back">
    <div class="brand brand--back">
      <span class="brand__mark"></span>
      <span class="brand__name">Paramount Hot Water Services</span>
    </div>
    <div class="panel panel--contact">
      <p>gareth@paramounthotwaterservices-example.com.au</p>
      <p>ABN 48207153690</p>
      <p>Licence No 538412K</p>
    </div>
    <div class="panel panel--services">
      <p class="services__title">Supply and installation of</p>
      <ul class="services__list">
        <li>electric storage</li>
        <li>gas storage/instantaneous</li>
        <li>heat pumps</li>
        <li>solar heaters</li>
      </ul>
    </div>
  </section>

</main>
</body>
</html>
```